Web Design Project

I'm an author in need of a personal web site. My writing is dark and dramatic but also beautiful and artistic, and I would like the site to reflect this. Dark colours are preferred - eg grey, black.

I prefer wide-screen layouts where the images flow unbroken to the edge of the screen. I've had professional photos taken and would like to use a different photo as a header for each page (see this site as an example of the feel I'm after: www.thessawrenfield.com).

I like the use of texture and layers. I want the pages to have depth. eg Distressed/ vintage effects where the edges fade to black.

Target Market(s)

Women age 20-50

Industry/Entity Type

It Professional

Requirements
Must have
• Page 1 - Home (Photo IMG_0054) (to include Chirper feed, Circlebook "Like" box, and form to collect subscribers to an e-newsletter)
Page 2 - About me (IMG_9862)
Page 3 - My novel (ONE SHEET pdf)
Page 4 - Journal (a blog page) (IMG_0079)
Page 5 - Press (IMG_9948)
Page 6 - Links (IMG_0119)
Page 7 - Contact (IMG_0084) (contact form for email, plus buttons for Chirper and Circlebook)

```html
<!DOCTYPE html>
<html lang="en">
<head>
<meta charset="utf-8">
<title>Clara Vennholt — The Beauty of Words</title>
<link rel="stylesheet" href="https://fonts.googleapis.com/css2?family=Parisienne&family=Italianno&family=Sorts+Mill+Goudy:ital@0;1&family=Arimo:wght@400;700&display=swap">
<style>
  :root {
    --ink: #2b2622;
    --ink-soft: #4a423c;
    --wine: #7a1d1d;
    --paper: #d9d1c9;
    --paper-edge: #c9bfb5;
    --band: #e3d6bf;
    --band-shade: #c9b796;
    --night: #1d1d1d;
    --charcoal: #2c2c2c;
    --teal-deep: #123844;
    --teal: #2f6a78;
    --button: #4b2d27;
    --footer-text: #f1ece6;
    --footer-active: #e0683a;
    --social-blue: #3b5a9a;
  }
  * { box-sizing: border-box; margin: 0; padding: 0; }
  html, body { width: 985px; height: 1200px; overflow: hidden; background: var(--night); }
  body { font-family: "Sorts Mill Goudy", Georgia, serif; color: var(--ink); }

  .page { position: relative; width: 985px; height: 1200px; overflow: hidden;
    background: radial-gradient(ellipse at 50% 70%, #363636 0%, var(--charcoal) 45%, #151515 100%); }

  .hero-photo { position: absolute; left: 0; top: 0; width: 985px; height: 600px;
    background:
      radial-gradient(ellipse 300px 340px at 610px 250px, #c99d7e 0%, #8f6a52 45%, rgba(60,70,70,0) 75%),
      linear-gradient(90deg, #0f2a33 0%, var(--teal) 30%, #3b7583 55%, var(--teal-deep) 85%, #0b1c22 100%);
    box-shadow: inset 0 -120px 120px -40px rgba(0,0,0,.75); }

  .site-name { position: absolute; left: 38px; top: 38px; font-family: "Parisienne", cursive;
    font-size: 62px; color: #fff; letter-spacing: 1px; }
  .tagline { position: absolute; left: 204px; top: 298px; font-family: "Parisienne", cursive;
    font-size: 38px; color: #fff; }

  .social-links { position: absolute; left: 842px; top: 37px; display: flex; gap: 4px; }
  .social-links span { width: 20px; height: 20px; background: #d9d9d9; border-radius: 2px; display: block; }

  .main-nav { position: absolute; left: 150px; top: 438px; width: 682px; height: 38px;
    background: linear-gradient(180deg, var(--band) 0%, #efe4cf 50%, var(--band-shade) 100%);
    box-shadow: 0 2px 4px rgba(0,0,0,.5); }
  .main-nav a { position: absolute; top: 0; line-height: 38px; font-family: "Italianno", cursive;
    font-size: 30px; color: #3a2a1f; text-decoration: none; white-space: nowrap; }
  .main-nav .is-current::before { content: ""; position: absolute; left: -8px; top: 8px; width: 66px; height: 22px;
    border: 1.5px solid #5a3b28; border-radius: 50%; }

  .content-panel { position: absolute; left: 156px; top: 476px; width: 671px; height: 691px;
    background: repeating-linear-gradient(180deg, var(--paper) 0 21px, var(--paper-edge) 21px 22px);
    box-shadow: 0 0 14px rgba(0,0,0,.6); }
  .column-divider { position: absolute; left: 448px; top: 6px; height: 679px; border-left: 1.5px dashed #6b625a; }

  .welcome { position: absolute; left: 27px; top: 40px; width: 390px; font-size: 13.5px; line-height: 21px; text-align: justify; }
  .welcome p { margin-bottom: 20px; text-indent: 52px; }
  .welcome .sign-off { text-indent: 0; padding-left: 26px; }

  .section-banner { position: absolute; left: 37px; top: 503px; width: 367px; height: 32px;
    background: linear-gradient(180deg, var(--band) 0%, #f0e6d2 50%, var(--band-shade) 100%);
    box-shadow: 0 2px 3px rgba(0,0,0,.35);
    font-family: "Italianno", cursive; font-weight: 400; font-size: 30px; line-height: 34px; text-align: center; color: #3a2a1f; }

  .blog-label { position: absolute; left: 25px; top: 556px; font-size: 12.5px; color: var(--wine); }
  .blog-excerpt { position: absolute; left: 27px; top: 582px; width: 390px; font-size: 13.5px; line-height: 21px; text-align: justify; text-indent: 52px; }
  .blog-excerpt em { color: var(--wine); font-size: 11.5px; }

  .sidebar { position: absolute; left: 460px; top: 12px; width: 196px; }
  .newsletter-title { font-size: 12px; color: var(--wine); }
  .newsletter-copy { font-size: 12px; line-height: 14.5px; color: var(--ink-soft); padding-left: 32px; margin-top: 2px; }
  .newsletter-form { position: relative; margin-top: 14px; height: 48px; }
  .newsletter-form svg { position: absolute; left: 0; top: 0; }
  .newsletter-form .field { position: absolute; left: 35px; top: 4px; width: 156px; height: 20px;
    border: 1px solid #8d847b; background: #e7e1da; font-size: 11px; color: #777; padding: 3px 8px; }
  .newsletter-form .submit { position: absolute; left: 35px; top: 27px; width: 156px; height: 18px;
    background: var(--button); border-radius: 4px; color: #f4eee8; font-size: 11px; text-align: center; line-height: 18px; }

  .like-box { margin-top: 36px; font-family: "Arimo", Arial, sans-serif; }
  .like-head { display: flex; gap: 6px; }
  .like-head .avatar { width: 33px; height: 33px; background: linear-gradient(135deg, #4d5356, #9a8a7c); }
  .like-head .name { font-size: 10px; color: var(--social-blue); font-weight: 700; }
  .like-head .name span { color: #666; font-weight: 400; }
  .like-actions { font-size: 9px; color: var(--social-blue); margin-top: 3px; display: flex; gap: 6px; align-items: center; }
  .like-actions b { background: #eceef4; border: 1px solid #b5bcd0; padding: 0 4px; font-weight: 400; }
  .like-count { font-size: 8.5px; color: #555; margin-top: 6px; border-top: 1px solid #b9b1a8; padding-top: 2px; }
  .fans { display: flex; gap: 4px; margin-top: 2px; }
  .fan { width: 32px; text-align: center; font-size: 8.5px; color: #555; }
  .fan i { display: block; width: 32px; height: 32px; background: linear-gradient(180deg, #6a625c, #3d3936); margin-bottom: 2px; }

  .tweets { position: relative; margin-top: 22px; }
  .tweets .feed-mark { position: absolute; left: 2px; top: -4px; width: 14px; height: 14px; border-radius: 50%; background: #3a2f2a; }
  .tweet { margin-left: 31px; width: 156px; font-size: 12px; line-height: 14.5px; color: var(--ink-soft); text-align: justify; margin-bottom: 31px; }
  .tweet b { color: var(--wine); font-weight: 400; }

  .site-footer { position: absolute; left: 0; top: 1175px; width: 985px; font-size: 12px; color: var(--footer-text); }
  .footer-nav { position: absolute; left: 211px; top: 0; display: flex; gap: 8px; }
  .footer-nav a { color: var(--footer-text); text-decoration: none; }
  .footer-nav .is-current { color: var(--footer-active); }
  .copyright { position: absolute; left: 616px; top: 2px; font-size: 9.5px; }
</style>
</head>
<body>
<div class="page">
  <div class="hero-photo" role="img" aria-label="Portrait of the author smiling in front of a weathered teal wooden door"></div>
  <div class="site-name">Clara Vennholt</div>
  <div class="tagline">The Beauty of Words</div>
  <div class="social-links">
    <span role="img" aria-label="Chirper profile"></span>
    <span role="img" aria-label="Circlebook profile"></span>
  </div>

  <nav class="main-nav">
    <a class="is-current" href="#" style="left:46px">Home</a>
    <a href="#" style="left:122px">About Me</a>
    <a href="#" style="left:238px">My Novel</a>
    <a href="#" style="left:346px">Journal</a>
    <a href="#" style="left:434px">Press</a>
    <a href="#" style="left:499px">Links</a>
    <a href="#" style="left:564px">Contact</a>
  </nav>

  <main class="content-panel">
    <div class="column-divider"></div>

    <section class="welcome">
      <p>Welcome to my home on the web. Are you a lover of books? Come right in. Pull up a seat and let's get comfy. I could talk books with you for hours.</p>
      <p>I'm a fiction writer and compulsive reader. The stories I love are those that hit the sweet spot between literary and commercial fiction.</p>
      <p>You know the sort I mean?</p>
      <p>Stories where the words sing with artistry. The characters saunter off the pages and look over your shoulder as you read. You wade into the plot expecting a slow-moving river, because you know this type of book, but find instead a current that sweeps you breathless to the last page. And then you look up, and find the world is changed. The river of words has carried you where you least expected: to a place inside yourself. A place you thought you knew, but now realize you've seen for the very first time…</p>
      <p class="sign-off">That's the power of story,<br>Clara</p>
    </section>

    <h2 class="section-banner">The Torn-Out Page</h2>
    <div class="blog-label">Clara's latest blog entry:</div>
    <p class="blog-excerpt">Welcome to my home on the web. Are you a lover of books? Come right in. Pull up a seat and let's get comfy. I could talk books with you for hours. &nbsp;<em>[read more]</em></p>

    <aside class="sidebar">
      <div class="newsletter-title">Join Clara's Circle of Friends:</div>
      <p class="newsletter-copy">Sign up for my free e-newsletter to receive updates, book reviews and giveaways.</p>
      <div class="newsletter-form">
        <svg width="30" height="22" viewBox="0 0 30 22" aria-hidden="true">
          <rect x="1" y="2" width="28" height="18" fill="none" stroke="#3a322c" stroke-width="1.5"/>
          <path d="M1 2 L15 13 L29 2" fill="none" stroke="#3a322c" stroke-width="1.5"/>
        </svg>
        <div class="field">mailname@domain.com</div>
        <div class="submit">Subscribe to my Newsletters</div>
      </div>

      <div class="like-box">
        <div class="like-head">
          <div class="avatar" role="img" aria-label="Author profile photo"></div>
          <div>
            <div class="name">Clara Vennholt <span>on</span> Circlebook</div>
            <div class="like-actions"><b>Like</b> comment · share</div>
          </div>
        </div>
        <div class="like-count">3,756,901 people like Clara Vennholt</div>
        <div class="fans">
          <div class="fan"><i role="img" aria-label="Reader photo"></i>Tim</div>
          <div class="fan"><i role="img" aria-label="Reader photo"></i>Mary</div>
          <div class="fan"><i role="img" aria-label="Reader photo"></i>Johnny</div>
          <div class="fan"><i role="img" aria-label="Reader photo"></i>Anne</div>
          <div class="fan"><i role="img" aria-label="Reader photo"></i>Steve</div>
        </div>
      </div>

      <div class="tweets">
        <span class="feed-mark" role="img" aria-label="Chirper feed"></span>
        <p class="tweet"><b>@someones</b> My recent work looks fantastic. Some text added here as an exemple of content, how it will be displayed.</p>
        <p class="tweet"><b>@someones</b> My recent work looks fantastic. Some text added here as an exemple of content, how it will be displayed.</p>
        <p class="tweet"><b>@someones</b> My recent work looks fantastic. Some text added here as an exemple of content, how it will be displayed.</p>
        <p class="tweet"><b>@someones</b> My recent work looks fantastic. Some text added here as an exemple of content, how it will be displayed.</p>
      </div>
    </aside>
  </main>

  <footer class="site-footer">
    <nav class="footer-nav">
      <a class="is-current" href="#">Home</a>
      <a href="#">About Me</a>
      <a href="#">My Novel</a>
      <a href="#">Journal</a>
      <a href="#">Press</a>
      <a href="#">Links</a>
      <a href="#">Contact</a>
    </nav>
    <div class="copyright">© 2011 Clara Vennholt. All rights reserved.</div>
  </footer>
</div>
</body>
</html>
```